Financial planning firm needs business card designed

Hello

I am looking to have a standard size business card designed for our agents. Attached is our logo.

Industry/Entity Type

Financial Service

Requirements
Must have
• Derek Follwell
• Mortgage Agent
• Investment Specialist
• Office Address: 7 Barlow Ave. W., Suite K205, Hamilton, ON L9P 5Q4
• Office Ph#: (905) 555-0143 x 318
• email: dfollwell@corvantwm.example
• www.corvantwm.example
• PRBA Lic# 40615
Nice to have
• On the back maybe put:
• 8% to 12% Fixed per year! Ask me how.

```html
<!DOCTYPE html>
<html lang="en">
<head>
<meta charset="utf-8">
<title>Corvant Wealth Management – Business Card</title>
<link href="https://fonts.googleapis.com/css2?family=Tinos:wght@400;700&display=swap" rel="stylesheet">
<style>
  :root {
    --ink-dark: #27232f;
    --teal: #22c1ac;
    --teal-deep: #1fa897;
    --paper: #f3f3f3;
    --text-dark: #2b2830;
    --text-light: #d9d9dc;
    --stage: #e6e4e0;
  }
  * { box-sizing: border-box; margin: 0; padding: 0; }
  html, body {
    width: 1200px; height: 800px; overflow: hidden;
    background: var(--stage);
    font-family: "Tinos", "Times New Roman", serif;
  }
  .sheet {
    width: 1200px; height: 800px;
    display: flex; flex-direction: column; align-items: center; justify-content: center;
    gap: 28px;
  }
  .card {
    position: relative;
    width: 630px; height: 360px;
    overflow: hidden;
    box-shadow: 0 6px 18px rgba(0,0,0,.18);
  }

  /* Back */
  .card-back { background: var(--ink-dark); color: var(--text-light); }
  .brand {
    position: absolute; left: 0; right: 0; top: 100px;
    display: flex; align-items: center; justify-content: center; gap: 22px;
  }
  .brand-mark { width: 64px; height: 64px; background: var(--teal); }
  .brand-name { color: var(--text-light); font-weight: 400; text-transform: uppercase; }
  .brand-name .word { display: block; font-size: 46px; letter-spacing: 9px; line-height: 1; }
  .brand-name .sub { display: block; font-size: 12px; letter-spacing: 5.5px; margin-top: 8px; padding-top: 6px; border-top: 1px solid var(--teal); }
  .tagline {
    position: absolute; left: 0; right: 0; top: 232px;
    text-align: center; font-size: 17px; color: var(--text-light);
  }

  /* Front */
  .card-front { background: var(--paper); color: var(--text-dark); }
  .sail-field { position: absolute; right: 0; top: 0; width: 320px; height: 250px; }
  .agent { position: absolute; left: 46px; top: 128px; }
  .agent-name {
    font-size: 27px; font-weight: 400; text-transform: uppercase; letter-spacing: .5px;
    padding-bottom: 5px; border-bottom: 1.5px solid var(--text-dark); width: 262px;
  }
  .agent-role { font-size: 11px; text-transform: uppercase; letter-spacing: .6px; margin-top: 5px; line-height: 1.35; }
  .contact { position: absolute; left: 46px; top: 214px; font-size: 15.5px; line-height: 1.32; }
  .contact .line { display: flex; align-items: center; gap: 6px; }
  .contact .icon { width: 14px; height: 14px; fill: var(--text-dark); flex: none; }
  .contact .address { margin-bottom: 6px; }
  .footer-band {
    position: absolute; left: 0; right: 0; bottom: 0; height: 40px;
    background: var(--ink-dark); color: var(--text-light);
    display: flex; align-items: center; justify-content: flex-end;
    padding-right: 30px; font-size: 15px; letter-spacing: 1px;
  }
</style>
</head>
<body>
<main class="sheet">

  <section class="card card-back" aria-label="Card back">
    <div class="brand">
      <span class="brand-mark" aria-hidden="true"></span>
      <div class="brand-name">
        <span class="word">Corvant</span>
        <span class="sub">Wealth Management</span>
      </div>
    </div>
    <p class="tagline">8% to 12% Fixed per year! Ask me how</p>
  </section>

  <section class="card card-front" aria-label="Card front">
    <svg class="sail-field" viewBox="0 0 320 250" role="img" aria-label="Large brand emblem decoration in teal">
      <path d="M0 250 L0 120 Q40 60 120 40 L320 0 L320 250 Z" fill="var(--teal)"/>
    </svg>

    <div class="agent">
      <h1 class="agent-name">Derek Follwell</h1>
      <p class="agent-role">Mortgage Agent<br>Investment Specialist</p>
    </div>

    <div class="contact">
      <p class="address">7 Barlow Ave. W., Suite K205,<br>Hamilton, ON L9P 5Q4</p>
      <p class="line">
        <svg class="icon" viewBox="0 0 14 14" aria-hidden="true"><path d="M1 2h12v10H1z M3 4v6h8V4z"/><rect x="4" y="5" width="3" height="2"/></svg>
        (905) 555-0143 x 318
      </p>
      <p class="line">
        <svg class="icon" viewBox="0 0 14 14" aria-hidden="true"><path d="M1 3h12v9H1z" /><path d="M1 3l6 5 6-5" fill="none" stroke="#f3f3f3" stroke-width="1.2"/></svg>
        dfollwell@corvantwm.example
      </p>
      <p>PRBA Lic# 40615</p>
    </div>

    <div class="footer-band">www.corvantwm.example</div>
  </section>

</main>
</body>
</html>
```